Refresh of The Marston Collective business card

Update business card design using existing primary logo. Names, numbers, etc. are too hard to read on current design.

Target Market(s)

We are a CPA firm.

Industry/Entity Type

Accountant

Contact Information for Business Card

update current card

Colors
0355a3
3176b5
85acd3
0792cd

Requirements
Must have
• Easier to read phone numbers and names
• Use existing logo
Nice to have
• We love our color scheme and current TMC logo. But the names and phone numbers are too small and card just look old and stale.

```html
<!DOCTYPE html>
<html lang="en">
<head>
<meta charset="utf-8">
<title>The Marston Collective – Business Card</title>
<link rel="stylesheet" href="https://fonts.googleapis.com/css2?family=Cinzel:wght@400;600&family=PT+Sans:wght@400;700&display=swap">
<style>
  :root {
    --navy: #0355a3;
    --mid-blue: #3176b5;
    --light-blue: #85acd3;
    --bright-blue: #0792cd;
    --stripe-grey: #6e6f71;
    --card-white: #f6f6f6;
    --page-bg: #e4e6ea;
    --ink-white: #ffffff;
  }
  * { box-sizing: border-box; margin: 0; padding: 0; }
  html, body { width: 1200px; height: 780px; overflow: hidden; }
  body {
    background: var(--page-bg);
    font-family: "PT Sans", Arial, sans-serif;
    position: relative;
  }
  .card {
    position: absolute;
    top: 235px;
    width: 540px;
    height: 310px;
    border-radius: 4px;
    overflow: hidden;
    box-shadow: 0 6px 18px rgba(0,0,0,0.18);
  }

  /* ---------- Front ---------- */
  .card-front { left: 40px; background: var(--card-white); }
  .front-white {
    position: absolute; left: 0; top: 0; width: 100%; height: 128px;
    background: linear-gradient(180deg, #ffffff 0%, #eeeeee 100%);
  }
  .name-stripe {
    position: absolute; left: 0; top: 128px; width: 100%; height: 38px;
    background: var(--stripe-grey);
    display: flex; align-items: center; padding-left: 26px;
  }
  .person-name {
    font-family: "Cinzel", Georgia, serif;
    font-weight: 600; font-size: 23px; letter-spacing: 1px;
    color: var(--ink-white);
  }
  .contact-band {
    position: absolute; left: 0; top: 166px; width: 100%; height: 144px;
    background: linear-gradient(90deg, var(--navy) 0%, var(--bright-blue) 55%, var(--mid-blue) 100%);
    padding: 14px 26px;
  }
  .contact-list { list-style: none; }
  .contact-list li {
    display: flex; align-items: center; gap: 8px;
    color: var(--ink-white); font-size: 15px; line-height: 23px;
  }
  .contact-list svg { width: 16px; height: 16px; flex: none; }
  .address {
    color: var(--ink-white); font-size: 15px; margin-top: 2px; padding-left: 24px;
  }

  .brand-lockup {
    position: absolute; left: 26px; top: 34px;
    display: flex; align-items: center; gap: 14px;
  }
  .brand-dot {
    width: 58px; height: 58px; border-radius: 50%;
    background: var(--navy); border: 3px solid var(--light-blue);
  }
  .brand-name {
    font-family: "Cinzel", Georgia, serif; font-weight: 600;
    color: var(--navy); font-size: 22px; line-height: 1.1;
  }
  .brand-tagline {
    font-family: "Cinzel", Georgia, serif; font-weight: 600;
    color: var(--navy); font-size: 8px; letter-spacing: 2px; margin-top: 6px;
    text-transform: uppercase;
  }
  .front-seal {
    position: absolute; right: 22px; top: 18px;
    width: 150px; height: 150px; border-radius: 50%;
    background: radial-gradient(circle at 40% 35%, var(--mid-blue), var(--navy) 75%);
    border: 6px solid #ffffff;
    box-shadow: 0 0 0 3px var(--stripe-grey);
  }

  /* ---------- Back ---------- */
  .card-back {
    left: 620px;
    background: radial-gradient(ellipse at 50% 45%, var(--bright-blue) 0%, var(--mid-blue) 35%, var(--navy) 80%);
    display: flex; flex-direction: column; align-items: center; justify-content: center;
  }
  .back-lockup { display: flex; align-items: center; gap: 16px; }
  .back-lockup .brand-dot { background: #ffffff; border-color: var(--light-blue); width: 66px; height: 66px; }
  .back-lockup .brand-name,
  .back-lockup .brand-tagline { color: var(--ink-white); }
  .back-lockup .brand-name { font-size: 26px; }
  .back-rule { width: 230px; height: 1px; background: var(--ink-white); margin-top: 6px; }
  .website {
    margin-top: 34px; color: var(--ink-white); font-size: 16px; letter-spacing: 0.5px;
  }
</style>
</head>
<body>

<section class="card card-front" aria-label="Business card front">
  <div class="front-white"></div>
  <div class="brand-lockup">
    <span class="brand-dot"></span>
    <div>
      <div class="brand-name">The Marston<br>Collective</div>
      <div class="brand-tagline">Certified Public Accountants</div>
    </div>
  </div>
  <div class="front-seal"></div>

  <div class="name-stripe">
    <span class="person-name">ELENA R. MARSTON, CPA</span>
  </div>

  <div class="contact-band">
    <ul class="contact-list">
      <li>
        <svg viewBox="0 0 16 16" aria-hidden="true"><circle cx="8" cy="8" r="8" fill="#fff"/><path d="M5 4.5c.5-.5 1-.4 1.3 0l.7 1.2c.2.4 0 .8-.3 1l-.4.3c.4.9 1.1 1.6 2 2l.3-.4c.3-.3.7-.5 1-.3l1.2.7c.4.3.5.8 0 1.3-.6.6-1.5.8-2.4.3C6.6 9.6 5.6 8.6 4.7 6.9c-.5-.9-.3-1.8.3-2.4z" fill="#0355a3"/></svg>
        555.210.4487
      </li>
      <li>
        <svg viewBox="0 0 16 16" aria-hidden="true"><circle cx="8" cy="8" r="8" fill="#fff"/><rect x="5" y="4" width="6" height="3" fill="#0355a3"/><rect x="4" y="7" width="8" height="4" rx="1" fill="#0355a3"/><rect x="5.5" y="9.5" width="5" height="2.5" fill="#fff" stroke="#0355a3" stroke-width=".6"/></svg>
        555.210.4490
      </li>
      <li>
        <svg viewBox="0 0 16 16" aria-hidden="true"><circle cx="8" cy="8" r="8" fill="#fff"/><rect x="5.5" y="3.5" width="5" height="9" rx="1" fill="#0355a3"/><rect x="6.3" y="4.5" width="3.4" height="5.5" fill="#fff"/></svg>
        555.386.1172
      </li>
      <li>
        <svg viewBox="0 0 16 16" aria-hidden="true"><circle cx="8" cy="8" r="8" fill="#fff"/><rect x="4" y="5" width="8" height="6" fill="#0355a3"/><path d="M4 5l4 3.2L12 5" fill="none" stroke="#fff" stroke-width=".8"/></svg>
        elena@marstoncollective.com
      </li>
    </ul>
    <p class="address">118 Harbor Oak Dr. Suite 310 Lakewood, Ohio 44107</p>
  </div>
</section>

<section class="card card-back" aria-label="Business card back">
  <div class="back-lockup">
    <span class="brand-dot"></span>
    <div>
      <div class="brand-name">The Marston<br>Collective</div>
      <div class="back-rule"></div>
      <div class="brand-tagline">Certified Public Accountants</div>
    </div>
  </div>
  <p class="website">www.marstoncollective.com</p>
</section>

</body>
</html>
```